Website Design für Reinigungsunternehmen
Zielgruppe
Wir sind ein Reinigungsunternehmen, dass seit 2014 am Markt ist.
Was machen wir:
Das Angebot besteht darin, Räume nach dem IFSG (Infektionsschutzgesetz) und den Richtlinien des Helmut Brandis Instituts mit ausgewählten Verfahren keimfrei zu bekommen.
Hygiene und prophylaktische Desinfektion sind für die Nutzung stark frequentierter Räume und Oberflächen gerade jetzt essentiell, denn die Ausbreitung von Viren und Bakterien kann auch durch präventive Maßnahmen eingedämmt werden.
Das Angebot ist, mit speziellen Reinigungsverfahren in Kombination mit Kaltverneblung ,die Räume fast vollständig von Keimen, Viren und Bakterien zu befreien.
So ist auch die Desinfektion von schwer zugänglichen Stellen und Gegenständen gewährleistet. Die eingesetzte Kaltnebeltechnologie wirkt in Verbindung mit Wasserstoffperoxid in verschiedenen Konzentrationen sowohl bakterizid, viruzid als auch fungizid. Wasserstoffperoxid wird rückstandsfrei abgebaut. Nach einer Einwirkzeit kann der behandelte, desinfizierte Raum sofort mechanisch gelüftet werden – ohne Material oder Umweltschäden zu riskieren.
Hier ein kurzes und erklärendes Video: https://clipvault-demo.de/Qw7TnRpLx2a
Aufgabenstellung
Die Website Soll maximal 3 Seiten haben.. Home (bzw. was wir machen..) Über uns (wer wir sind..) und Kontakt (-daten.
Ich möchte relativ kurz und knapp zum Thema kommen. Wenig Text, nur das wesentliche auf den Punkt gebracht - dafür ein ansprechendes professionelles Design. Bitte keine Bilder mit Gebäude, Reiniger etc. - dafür andere kreative Assoziationen einbringen.

```html
<!DOCTYPE html>
<html lang="de">
<head>
<meta charset="utf-8">
<title>nuvelaq – Innovative Hygienekonzepte</title>
<link href="https://fonts.googleapis.com/css2?family=Montserrat:wght@400;500;600;700;800&display=swap" rel="stylesheet">
<style>
:root{
  --navy:#1f3360;
  --sky:#6aa9d4;
  --paper:#ffffff;
  --stage:#eeeeee;
  --footer:#f1f1f1;
  --ink:#1f3360;
}
*{box-sizing:border-box;margin:0;padding:0}
html,body{width:1200px;height:2945px;overflow:hidden;background:var(--stage);font-family:'Montserrat',sans-serif;color:var(--ink)}
.page{position:absolute;left:139px;width:922px;background:var(--paper);box-shadow:0 1px 2px rgba(0,0,0,.15);overflow:hidden}
.page-home{top:80px;height:922px}
.page-services{top:1039px;height:1117px}
.page-contact{top:2192px;height:672px}

.nav{position:absolute;top:20px;left:0;width:100%;display:flex;justify-content:center;gap:26px;font-size:9px;font-weight:600;letter-spacing:.3px}
.nav a{color:var(--navy);text-decoration:none;padding:6px 14px;border:1px solid transparent;border-radius:14px}
.nav a.active{color:var(--sky);border-color:var(--sky)}

.brand{position:absolute;left:0;width:100%;display:flex;justify-content:center;align-items:center;gap:10px}
.brand-dot{width:34px;height:34px;border-radius:50%;background:var(--sky)}
.brand-name{font-size:40px;font-weight:500;color:var(--navy);letter-spacing:-1px;line-height:1}

.splash{position:absolute;background:linear-gradient(160deg,rgba(106,169,212,.15),rgba(106,169,212,.55),rgba(31,51,96,.25));border-radius:40% 60% 50% 50%/60% 40% 60% 40%;opacity:.8}

.hero-title{position:absolute;left:0;width:100%;text-align:center}
.hero-title .line1{display:block;font-size:46px;font-weight:800;color:var(--navy);line-height:44px}
.hero-title .line2{display:block;font-size:29px;font-weight:700;color:var(--sky);line-height:32px;letter-spacing:.5px}
.hero-text{position:absolute;top:287px;left:0;width:100%;text-align:center;font-size:11px;font-weight:500;line-height:13px}
.hero-text b{color:var(--sky);font-weight:700}
.btn{position:absolute;top:360px;left:417px;width:88px;height:24px;border-radius:12px;background:var(--sky);color:#fff;font-size:8px;font-weight:700;display:flex;align-items:center;justify-content:center;box-shadow:0 2px 4px rgba(0,0,0,.15)}

.band{position:absolute;left:0;width:100%;background:var(--navy)}
.teaser{position:absolute;top:79px;width:177px;height:177px;border-radius:20px;background:var(--sky);color:#fff;padding:20px 20px}
.teaser.light{background:#fff;color:var(--sky)}
.icon{width:30px;height:30px;display:block}
.teaser h3{margin-top:12px;font-size:13.5px;font-weight:700;line-height:12px}
.teaser p{margin-top:12px;font-size:7px;line-height:8px;font-weight:400}
.teaser .more{position:absolute;left:21px;bottom:24px;font-size:8.5px;font-weight:700;display:flex;align-items:center;gap:8px}

.footer{position:absolute;left:0;width:100%;height:145px;background:var(--footer)}
.f-brand{position:absolute;left:181px;top:22px;display:flex;align-items:center;gap:4px}
.f-brand .brand-dot{width:14px;height:14px}
.f-brand .brand-name{font-size:18px}
.f-address{position:absolute;left:181px;top:55px;font-size:7px;line-height:8px}
.f-address b{color:var(--sky);font-weight:600}
.f-col{position:absolute;top:28px;font-size:7px}
.f-col h4{font-size:6.5px;font-weight:700;margin-bottom:15px}
.f-col li{list-style:none;height:16px;display:flex;align-items:center;gap:5px}
.f-col svg{width:8px;height:8px}
.f-input{width:130px;height:23px;border-radius:4px;background:#ddd;display:flex;align-items:center;justify-content:space-between;padding:0 8px;font-size:7px;color:#aaa;font-style:italic}
.f-note{margin-top:6px;width:130px;font-size:6px;line-height:6.5px}
.f-rule{position:absolute;left:181px;width:560px;top:120px;border-top:1px solid #ddd}
.f-copy{position:absolute;left:0;width:100%;top:130px;text-align:center;font-size:5.5px;font-weight:500}
.f-copy b{color:var(--sky);font-weight:600}

.intro-label{position:absolute;top:167px;left:181px;font-size:9px;font-weight:700}
.intro-text{position:absolute;top:190px;left:181px;width:305px;font-size:8px;line-height:9.4px}

.service{position:absolute;width:416px;height:176px;border-radius:20px;background:var(--sky);color:#fff;overflow:hidden}
.service.light{background:#fff;color:var(--sky)}
.service .icon{position:absolute;left:20px;top:19px}
.service h3{position:absolute;left:62px;top:27px;font-size:13.5px;font-weight:700}
.service .body{position:absolute;left:62px;top:61px;width:210px;font-size:6.8px;line-height:8px}
.service .body p+p{margin-top:6px}
.service ul{position:absolute;left:290px;top:61px;font-size:7px;line-height:11.8px;list-style:none}
.service li::before{content:"";display:inline-block;width:5px;height:5px;border-radius:50%;background:currentColor;margin-right:6px;vertical-align:middle}
.service .back{position:absolute;left:370px;top:140px;width:12px;height:10px}
.service .ring{position:absolute;left:260px;top:40px;width:170px;height:170px;border-radius:50%;border:16px solid rgba(255,255,255,.12)}
.service.light .ring{border-color:rgba(106,169,212,.1)}

.cta{position:absolute;left:0;width:100%;text-align:center}
.cta .line1{display:block;font-size:47px;font-weight:800;color:var(--navy);line-height:44px}
.cta .line2{display:block;font-size:32px;font-weight:700;color:var(--sky);line-height:38px;letter-spacing:.5px}
.cta-call{position:absolute;left:438px;top:1022px;width:46px;height:46px;border-radius:50%;background:var(--sky);display:flex;align-items:center;justify-content:center}

.contact-list{position:absolute;left:0;width:100%;display:flex;flex-direction:column;align-items:center;gap:17px}
.contact-row{display:flex;align-items:center;gap:16px;color:#fff;font-size:26px;font-weight:600}
.contact-row .circle{width:44px;height:44px;border-radius:50%;background:var(--sky);display:flex;align-items:center;justify-content:center}
</style>
</head>
<body>

<section class="page page-home">
  <nav class="nav"><a class="active">HOME</a><a>LEISTUNGEN</a><a>KONTAKT</a></nav>
  <div class="splash" role="img" aria-label="Wasserspritzer, vertikal" style="left:120px;top:0;width:150px;height:410px"></div>
  <div class="splash" role="img" aria-label="Wasserspritzer, vertikal" style="left:645px;top:25px;width:135px;height:410px"></div>
  <div class="brand" style="top:110px"><span class="brand-dot"></span><span class="brand-name">nuvelaq</span></div>
  <h1 class="hero-title" style="top:190px"><span class="line1">INNOVATIVE</span><span class="line2">HYGIENEKONZEPTE</span></h1>
  <p class="hero-text">Wir schließen Reinigungslücken und befreien<br>Ihre Räumlichkeiten zu <b>99,9 %</b> von<br><b>Viren, Bakterien und Keimen</b></p>
  <div class="btn">LERN MEHR</div>

  <div class="band" style="top:442px;height:336px">
    <article class="teaser" style="left:181px">
      <svg class="icon" viewBox="0 0 30 30" fill="none" stroke="currentColor" stroke-width="1.8"><path d="M26 15a11 11 0 1 1-4-8.5"/><path d="M22 3v4h-4"/><path d="M15 8c-3 4-4.5 6-4.5 8a4.5 4.5 0 0 0 9 0c0-2-1.5-4-4.5-8z" fill="currentColor" stroke="none"/></svg>
      <h3>Flächen- und Raumdesinfektion gem. IFSG § 17</h3>
      <p>Lorem ipsum dolor sit amet,<br>consectetur adipiscing elit</p>
      <span class="more">LERN MEHR <svg width="12" height="9" viewBox="0 0 12 9" fill="currentColor"><path d="M0 3.5h8V1l4 3.5L8 8V5.5H0z"/></svg></span>
    </article>
    <article class="teaser light" style="left:373px">
      <svg class="icon" viewBox="0 0 30 30" fill="none" stroke="currentColor" stroke-width="1.8"><path d="M26 15a11 11 0 1 1-4-8.5"/><path d="M22 3v4h-4"/><path d="M15 8c-3 4-4.5 6-4.5 8a4.5 4.5 0 0 0 9 0c0-2-1.5-4-4.5-8z" fill="currentColor" stroke="none"/></svg>
      <h3>HBI gelistete und geprüfte Verfahren</h3>
      <p>Lorem ipsum dolor sit amet,<br>consectetur adipiscing elit</p>
      <span class="more">LERN MEHR <svg width="12" height="9" viewBox="0 0 12 9" fill="currentColor"><path d="M0 3.5h8V1l4 3.5L8 8V5.5H0z"/></svg></span>
    </article>
    <article class="teaser" style="left:565px">
      <svg class="icon" viewBox="0 0 30 30" fill="none" stroke="currentColor" stroke-width="1.8"><path d="M26 15a11 11 0 1 1-4-8.5"/><path d="M22 3v4h-4"/><path d="M15 8c-3 4-4.5 6-4.5 8a4.5 4.5 0 0 0 9 0c0-2-1.5-4-4.5-8z" fill="currentColor" stroke="none"/></svg>
      <h3>Staatlich geprüfte Desinfektoren</h3>
      <p>Lorem ipsum dolor sit amet,<br>consectetur adipiscing elit</p>
      <span class="more">LERN MEHR <svg width="12" height="9" viewBox="0 0 12 9" fill="currentColor"><path d="M0 3.5h8V1l4 3.5L8 8V5.5H0z"/></svg></span>
    </article>
  </div>

  <footer class="footer" style="top:778px">
    <div class="f-brand"><span class="brand-dot"></span><span class="brand-name">nuvelaq</span></div>
    <div class="f-address"><b>NUVELAQ GROUP</b><br>Gebäudereinigung &amp; Hygienekonzepte<br>Lindenweg 4<br>00000 Musterfeld</div>
    <div class="f-col" style="left:372px"><h4>QUICK LINKS</h4><ul><li>HOME</li><li>LEISTUNGEN</li><li>KONTAKT</li></ul></div>
    <div class="f-col" style="left:468px"><h4>KONTAKT UNS</h4><ul>
      <li><svg viewBox="0 0 10 10" fill="#6aa9d4"><path d="M2 0l2 2.5-1 1.2c.7 1.4 1.8 2.5 3.2 3.2l1.2-1L10 8 8.5 10C4 9.5.5 6 0 1.5z"/></svg>01234 / 567 890 10</li>
      <li><svg viewBox="0 0 10 10" fill="#6aa9d4"><rect x="2" y="0" width="6" height="4"/><rect x="1" y="4" width="8" height="6" rx="1"/></svg>01234 / 567 890 19</li>
      <li><svg viewBox="0 0 10 10" fill="#6aa9d4"><path d="M0 2h10v6H0z"/><path d="M0 2l5 3.5L10 2" stroke="#fff" fill="none"/></svg>mail@nuvelaq.example</li></ul></div>
    <div class="f-col" style="left:612px"><h4>NEWSLETTER</h4><div class="f-input">Email address <svg viewBox="0 0 10 8" width="9" height="7" fill="#6aa9d4"><path d="M0 0h10v8H0z"/></svg></div><p class="f-note">Lorem ipsum dolor sit amet, consectetur adipiscing elit</p></div>
    <div class="f-rule"></div>
    <div class="f-copy">ALL RIGHTS RESERVED BY <b>NUVELAQ GROUP</b></div>
  </footer>
</section>

<section class="page page-services">
  <nav class="nav"><a>HOME</a><a class="active">LEISTUNGEN</a><a>KONTAKT</a></nav>
  <div class="brand" style="top:94px"><span class="brand-dot"></span><span class="brand-name">nuvelaq</span></div>
  <h2 class="intro-label">NUVELAQ GROUP</h2>
  <p class="intro-text">Sed ut perspiciatis unde omnis iste natus error sit voluptatem accusantium doloremque laudantium, totam rem aperiam, eaque ipsa quae ab illo inventore veritatis et quasi architecto beatae vitae dicta sunt explicabo. Nemo enim ipsam voluptatem quia voluptas sit aspernatur aut odit aut fugit, sed quia consequuntur magni dolores eos qui ratione voluptatem sequi nesciunt.</p>

  <div class="band" style="top:259px;height:647px">
    <article class="service" style="left:181px;top:31px">
      <span class="ring"></span>
      <svg class="icon" viewBox="0 0 30 30" fill="none" stroke="currentColor" stroke-width="1.8"><path d="M26 15a11 11 0 1 1-4-8.5"/><path d="M22 3v4h-4"/><path d="M15 8c-3 4-4.5 6-4.5 8a4.5 4.5 0 0 0 9 0c0-2-1.5-4-4.5-8z" fill="currentColor" stroke="none"/></svg>
      <h3>Flächen- und Raumdesinfektion gem. IFSG § 17</h3>
      <div class="body"><p>Sed ut perspiciatis unde omnis iste natus error sit voluptatem accusantium doloremque laudantium, totam rem aperiam, eaque ipsa quae ab illo inventore veritatis et quasi architecto beatae vitae dicta sunt explicabo. Nemo enim ipsam voluptatem quia voluptas sit aspernatur aut odit aut fugit, sed quia consequuntur magni dolores eos qui ratione voluptatem sequi nesciunt.</p><p>Neque porro quisquam est, qui dolorem ipsum quia dolor sit amet, consectetur, adipisci velit, sed quia non numquam eius modi tempora incidunt ut labore et dolore magnam aliquam</p></div>
      <ul><li>Sed ut perspiciatis</li><li>Voluptatem accusantium</li><li>Neque</li><li>Nemo enim ipsam</li><li>consectetur, adipisci velit</li></ul>
      <svg class="back" viewBox="0 0 12 10" fill="currentColor"><path d="M12 4H4V1L0 5l4 4V6h8z"/></svg>
    </article>
    <article class="service light" style="left:324px;top:232px">
      <span class="ring"></span>
      <svg class="icon" viewBox="0 0 30 30" fill="none" stroke="currentColor" stroke-width="1.8"><path d="M26 15a11 11 0 1 1-4-8.5"/><path d="M22 3v4h-4"/><path d="M15 8c-3 4-4.5 6-4.5 8a4.5 4.5 0 0 0 9 0c0-2-1.5-4-4.5-8z" fill="currentColor" stroke="none"/></svg>
      <h3>Staatlich geprüfte Desinfektoren</h3>
      <div class="body"><p>Sed ut perspiciatis unde omnis iste natus error sit voluptatem accusantium doloremque laudantium, totam rem aperiam, eaque ipsa quae ab illo inventore veritatis et quasi architecto beatae vitae dicta sunt explicabo. Nemo enim ipsam voluptatem quia voluptas sit aspernatur aut odit aut fugit, sed quia consequuntur magni dolores eos qui ratione voluptatem sequi nesciunt.</p><p>Neque porro quisquam est, qui dolorem ipsum quia dolor sit amet, consectetur, adipisci velit, sed quia non numquam eius modi tempora incidunt ut labore et dolore magnam aliquam</p></div>
      <ul><li>Sed ut perspiciatis</li><li>Voluptatem accusantium</li><li>Neque</li><li>Nemo enim ipsam</li><li>consectetur, adipisci velit</li></ul>
      <svg class="back" viewBox="0 0 12 10" fill="currentColor"><path d="M12 4H4V1L0 5l4 4V6h8z"/></svg>
    </article>
    <article class="service" style="left:181px;top:439px">
      <span class="ring"></span>
      <svg class="icon" viewBox="0 0 30 30" fill="none" stroke="currentColor" stroke-width="1.8"><path d="M26 15a11 11 0 1 1-4-8.5"/><path d="M22 3v4h-4"/><path d="M15 8c-3 4-4.5 6-4.5 8a4.5 4.5 0 0 0 9 0c0-2-1.5-4-4.5-8z" fill="currentColor" stroke="none"/></svg>
      <h3>Staatlich geprüfte Desinfektoren</h3>
      <div class="body"><p>Sed ut perspiciatis unde omnis iste natus error sit voluptatem accusantium doloremque laudantium, totam rem aperiam, eaque ipsa quae ab illo inventore veritatis et quasi architecto beatae vitae dicta sunt explicabo. Nemo enim ipsam voluptatem quia voluptas sit aspernatur aut odit aut fugit, sed quia consequuntur magni dolores eos qui ratione voluptatem sequi nesciunt.</p><p>Neque porro quisquam est, qui dolorem ipsum quia dolor sit amet, consectetur, adipisci velit, sed quia non numquam eius modi tempora incidunt ut labore et dolore magnam aliquam</p></div>
      <ul><li>Sed ut perspiciatis</li><li>Voluptatem accusantium</li><li>Neque</li><li>Nemo enim ipsam</li><li>consectetur, adipisci velit</li></ul>
      <svg class="back" viewBox="0 0 12 10" fill="currentColor"><path d="M12 4H4V1L0 5l4 4V6h8z"/></svg>
    </article>
  </div>

  <h2 class="cta" style="top:926px"><span class="line1">HANDELN SIE JETZT</span><span class="line2">UND KONTAKTIEREN SIE UNS</span></h2>
  <div class="cta-call"><svg width="20" height="20" viewBox="0 0 10 10" fill="#fff"><path d="M2 0l2 2.5-1 1.2c.7 1.4 1.8 2.5 3.2 3.2l1.2-1L10 8 8.5 10C4 9.5.5 6 0 1.5z"/></svg></div>
  <div class="f-rule" style="top:1093px"></div>
  <div class="f-copy" style="top:1103px">ALL RIGHTS RESERVED BY <b>NUVELAQ GROUP</b></div>
</section>

<section class="page page-contact">
  <nav class="nav"><a>HOME</a><a>LEISTUNGEN</a><a class="active">KONTAKT</a></nav>
  <div class="splash" role="img" aria-label="Wasserwelle, horizontal" style="left:0;top:90px;width:341px;height:110px"></div>
  <div class="splash" role="img" aria-label="Wasserwelle, horizontal" style="left:578px;top:85px;width:344px;height:115px"></div>
  <div class="brand" style="top:95px"><span class="brand-dot"></span><span class="brand-name">nuvelaq</span></div>

  <div class="band" style="top:260px;height:268px">
    <div class="contact-list" style="top:82px">
      <div class="contact-row"><span class="circle"><svg width="20" height="20" viewBox="0 0 10 10" fill="#fff"><path d="M2 0l2 2.5-1 1.2c.7 1.4 1.8 2.5 3.2 3.2l1.2-1L10 8 8.5 10C4 9.5.5 6 0 1.5z"/></svg></span>01234 / 567 890 10</div>
      <div class="contact-row"><span class="circle"><svg width="20" height="16" viewBox="0 0 10 8" fill="#fff"><path d="M0 0h10v8H0z"/><path d="M0 0l5 4 5-4" stroke="#6aa9d4" fill="none"/></svg></span>mail@nuvelaq.example</div>
    </div>
  </div>

  <footer class="footer" style="top:528px">
    <div class="f-brand"><span class="brand-dot"></span><span class="brand-name">nuvelaq</span></div>
    <div class="f-address"><b>NUVELAQ GROUP</b><br>Gebäudereinigung &amp; Hygienekonzepte<br>Lindenweg 4<br>00000 Musterfeld</div>
    <div class="f-col" style="left:372px"><h4>QUICK LINKS</h4><ul><li>HOME</li><li>LEISTUNGEN</li><li>KONTAKT</li></ul></div>
    <div class="f-col" style="left:468px"><h4>KONTAKT UNS</h4><ul>
      <li><svg viewBox="0 0 10 10" fill="#6aa9d4"><path d="M2 0l2 2.5-1 1.2c.7 1.4 1.8 2.5 3.2 3.2l1.2-1L10 8 8.5 10C4 9.5.5 6 0 1.5z"/></svg>01234 / 567 890 10</li>
      <li><svg viewBox="0 0 10 10" fill="#6aa9d4"><rect x="2" y="0" width="6" height="4"/><rect x="1" y="4" width="8" height="6" rx="1"/></svg>01234 / 567 890 19</li>
      <li><svg viewBox="0 0 10 10" fill="#6aa9d4"><path d="M0 2h10v6H0z"/><path d="M0 2l5 3.5L10 2" stroke="#fff" fill="none"/></svg>mail@nuvelaq.example</li></ul></div>
    <div class="f-col" style="left:612px"><h4>NEWSLETTER</h4><div class="f-input">Email address <svg viewBox="0 0 10 8" width="9" height="7" fill="#6aa9d4"><path d="M0 0h10v8H0z"/></svg></div><p class="f-note">Lorem ipsum dolor sit amet, consectetur adipiscing elit</p></div>
    <div class="f-rule"></div>
    <div class="f-copy">ALL RIGHTS RESERVED BY <b>NUVELAQ GROUP</b></div>
  </footer>
</section>

</body>
</html>
```